Carpet cleaning company wants business card

Need an exciting new fresh design for business cards for my carpet cleaning /pest control business
www.tidewellhomecare.com.au
Can design include a lined section for quoting or information? Thanks !

```html
<!DOCTYPE html>
<html lang="en">
<head>
<meta charset="utf-8">
<title>Tidewell Home Care – Business Card</title>
<link rel="stylesheet" href="https://fonts.googleapis.com/css2?family=Arimo:wght@400;700&display=swap">
<style>
  :root {
    --stage: #2b2b2d;
    --card: #1d1d1f;
    --card-pattern: #161617;
    --edge: #e63a30;
    --brand-blue: #0a5cb8;
    --brand-red: #e63a30;
    --ink: #f2f2f2;
    --rule: #cfcfcf;
  }
  * { box-sizing: border-box; margin: 0; padding: 0; }
  html, body {
    width: 1200px; height: 970px; overflow: hidden;
    background: var(--stage);
    font-family: "Arimo", Arial, sans-serif;
  }
  .stage {
    width: 1200px; height: 970px;
    display: flex; flex-direction: column; align-items: center; justify-content: center;
    gap: 40px;
  }
  .card {
    position: relative;
    width: 740px; height: 423px;
    background: var(--card);
    border-left: 4px solid var(--edge);
    border-bottom: 4px solid var(--edge);
    overflow: hidden;
  }
  /* back side */
  .card-back .texture {
    position: absolute; inset: 0;
    background: linear-gradient(135deg, var(--card-pattern) 0%, #232325 55%, #2e2e30 100%);
  }
  .card-back .back-brand {
    position: absolute; left: 50%; top: 50%;
    transform: translate(-50%, -50%);
    display: flex; align-items: center; gap: 12px;
    font-weight: 700; font-size: 34px; color: var(--brand-red);
    white-space: nowrap;
  }
  .brand-mark {
    width: 22px; height: 22px; border-radius: 50%;
    background: var(--brand-blue);
  }
  /* front side */
  .front-brand {
    position: absolute; left: 0; right: 0; top: 78px;
    display: flex; justify-content: center; align-items: center; gap: 16px;
    font-weight: 700; font-size: 54px; color: var(--brand-blue);
    white-space: nowrap;
  }
  .front-brand .brand-mark { width: 36px; height: 36px; background: var(--brand-red); }
  .details {
    position: absolute; left: 0; right: 0; top: 196px;
    display: flex; justify-content: center; align-items: stretch; gap: 26px;
  }
  .person { text-align: right; padding-top: 36px; }
  .person-name {
    font-weight: 700; font-size: 22px; color: var(--brand-red);
    letter-spacing: 0.5px;
  }
  .person-role { font-size: 17px; color: var(--ink); margin-top: 2px; }
  .divider { width: 1px; background: var(--rule); }
  .contacts { list-style: none; display: flex; flex-direction: column; gap: 5px; }
  .contacts li {
    display: flex; align-items: center; gap: 10px;
    font-size: 16px; color: var(--ink);
  }
  .contacts svg { width: 15px; height: 15px; flex: none; }
  .address {
    position: absolute; left: 0; right: 0; bottom: 52px;
    text-align: center; font-size: 16px; color: var(--ink);
  }
</style>
</head>
<body>
<main class="stage">
  <section class="card card-back" aria-label="Card back">
    <div class="texture" role="img" aria-label="Repeating embossed brand-name pattern in dark tones"></div>
    <div class="back-brand"><span class="brand-mark"></span>Tidewell Home Care</div>
  </section>

  <section class="card card-front" aria-label="Card front">
    <div class="front-brand"><span class="brand-mark"></span>Tidewell Home Care</div>
    <div class="details">
      <div class="person">
        <p class="person-name">MARCUS HALE</p>
        <p class="person-role">Manager</p>
      </div>
      <div class="divider"></div>
      <ul class="contacts">
        <li>
          <svg viewBox="0 0 16 16" fill="none" stroke="var(--brand-red)" stroke-width="1.6"><path d="M3 2h3l1.5 3.5-2 1.2a8 8 0 0 0 3.8 3.8l1.2-2L14 10v3a1 1 0 0 1-1 1A11 11 0 0 1 2 3a1 1 0 0 1 1-1z"/></svg>
          07 5550 1284
        </li>
        <li>
          <svg viewBox="0 0 16 16" fill="none" stroke="var(--brand-red)" stroke-width="1.6"><rect x="4" y="1" width="8" height="14" rx="1.5"/><line x1="7" y1="12.5" x2="9" y2="12.5"/></svg>
          0400 555 217
        </li>
        <li>
          <svg viewBox="0 0 16 16" fill="none" stroke="var(--brand-red)" stroke-width="1.6"><rect x="1.5" y="3.5" width="13" height="9"/><path d="M1.5 3.5 8 9l6.5-5.5"/></svg>
          admin@tidewellhomecare.com.au
        </li>
        <li>
          <svg viewBox="0 0 16 16" fill="none" stroke="var(--brand-red)" stroke-width="1.4"><circle cx="8" cy="8" r="6.5"/><ellipse cx="8" cy="8" rx="3" ry="6.5"/><line x1="1.5" y1="8" x2="14.5" y2="8"/></svg>
          www.tidewellhomecare.com.au
        </li>
      </ul>
    </div>
    <p class="address">Your Address, City, State, Zip 0000</p>
  </section>
</main>
</body>
</html>
```